Piano-centered Instrumental Jazz Album Needs Cover Artwork

The cover has five parts, each one has obligatory features:

I. Main cover

1. Title: Gentle Willow II.
2. Artist: Ember Reed Trio
3. Design image*

* The main design motive can be something that suggests the number 4 (quartet), the sun (sunlight, sun rays), music, piano, notes, nature… Can, but doesn’t have to be one or more of these. But it should represent what the title says.
* I prefer zen-like, minimalist solutions.
* NO stock images, please! Except for unrecognizable parts of something.

II. Cover inside

1. Track list (18 songs) with durations
2. All songs written by Bence Morvath
3. Copyright Velmorsound 2016.
4. Design image

III. Disc

1. Artist: Ember Reed Trio
2. Title: Gentle Willow II.
3. All songs written by Bence Morvath (round on the edge)
4. Copyright Velmorsound 2016. (round on the edge)
5. www.velmorsound.com (round on the edge)

IV. Cover back

1. Track list (same as cover inside)
4. www.velmorsound.com
5. design image (optional)
6. The paper of this page is longer than the main cover, because it is to be turned up when put in the CD case, and there is the saddle with the name of the Artist and Title of the album. On both ends.

V. Under the disc

1. No words, only some design feature.

Important:
The main cover I need in RGB and also CMYK, all the others only CMYK.
I need the work file (cdr, ai or whatever you use)
I need the CMYK images prepared for printing (sizes set, and that little extra on the edges).
I need the RGB main cover cover in jpeg, 3000x3000 pixels.
That's all. :)

The most important of these all is of course the main cover RGB. Do this one first!

Here’s a sample to listen, it might inspire you:

https://files.exampleshare.test/u/48301772/ember%20reed%20sample%2020160103.mp3

If you take a closer look at my website, you can see the whole concept.

Good luck and enjoy!
Regards,
Bence

Requirements
Must have
• Tracklist:
• 1 First, in G 05:08
• 2 Second, in Em 05:11
• 3 Third, in G 05:09
• 4 Fourth, in A 05:07
• 5 Fifth, in Bm 05:01
• 6 Sixth, in A 05:11
• 7 Seventh, in G 05:07
• 8 Eighth, in Bm 05:06
• 9 Ninth, in Gm 05:04
• 10 Tenth, in E 05:03
• 11 Eleventh, in G 05:12
• 12 Twelfth, in A 05:09
• 13 Thirteenth, in E 05:10
• 14 Fourteenth, in Am 05:14
• 15 Fifteenth, in F 05:05
• 16 Sixteenth, in Am 05:05
• 17 Seventeenth, in F 05:04
• 18 Eighteenth, in D 05:07
Should not have
• Stock images copy-pasted, additional copyright costs.

```html
<!DOCTYPE html>
<html lang="en">
<head>
<meta charset="utf-8">
<title>Gentle Willow II. — Ember Reed Trio</title>
<link href="https://fonts.googleapis.com/css2?family=Montserrat:ital,wght@0,300;0,400;0,700;0,800;1,400&display=swap" rel="stylesheet">
<style>
  :root{
    --backdrop:#ececec;
    --paper:#f3efe4;
    --paper-edge:#e6e0d0;
    --ink:#1d1d1d;
    --ink-soft:#4a4a4a;
    --sun-top:#f6a21c;
    --sun-mid:#f27d25;
    --sun-low:#ec4f3a;
    --wash-yellow:#f7c633;
    --wash-pink:#e23a6a;
    --tray:#f7f6f2;
    --tray-line:#d9d7d0;
  }
  *{box-sizing:border-box;margin:0;padding:0}
  html,body{width:1200px;height:1200px;overflow:hidden}
  body{
    background:var(--backdrop);
    font-family:"Montserrat",Arial,sans-serif;
    color:var(--ink);
    position:relative;
  }
  .panel{
    position:absolute;
    background:radial-gradient(ellipse at 40% 40%,var(--paper) 60%,var(--paper-edge) 100%);
    overflow:hidden;
    box-shadow:0 2px 6px rgba(0,0,0,.12);
  }
  .sun-art{position:absolute;display:block}
  .front-cover{left:140px;top:172px;width:408px;height:392px}
  .back-cover{left:644px;top:172px;width:448px;height:392px}
  .inside-cover{left:32px;top:620px;width:416px;height:404px}
  .tray{
    position:absolute;left:448px;top:620px;width:480px;height:404px;
    background:var(--tray);overflow:hidden;
    box-shadow:0 2px 6px rgba(0,0,0,.12);
  }

  .album-title{font-weight:400;line-height:1.1;white-space:nowrap}
  .album-artist{font-weight:300;line-height:1.1;white-space:nowrap;color:#333}

  .front-cover .heading{position:absolute;left:0;right:0;top:292px;text-align:center}
  .front-cover .album-title{font-size:19px}
  .front-cover .album-artist{font-size:29px}

  .side-heading{position:absolute;text-align:right;white-space:nowrap}
  .side-heading .album-title{font-size:14px}
  .side-heading .album-artist{font-size:22px;margin-bottom:8px}
  .credits{font-size:9.5px;line-height:1.45;color:var(--ink-soft)}
  .back-cover .side-heading{right:200px;top:256px}
  .inside-cover .side-heading{right:206px;top:262px}

  .web-address{position:absolute;left:126px;top:362px;font-size:11.5px;font-weight:700;letter-spacing:.4px}

  .track-list{position:absolute;list-style:none;font-size:9px;color:var(--ink-soft)}
  .track-list li{display:grid;grid-template-columns:16px 94px 32px;height:15px;align-items:center;white-space:nowrap}
  .track-no{font-weight:800;color:var(--ink);text-align:right;padding-right:5px}
  .track-time{font-style:italic}
  .back-cover .track-list{left:282px;top:66px}
  .inside-cover .track-list{left:244px;top:78px}

  .disc{position:absolute;left:770px;top:690px;width:420px;height:420px}
</style>
</head>
<body>

<section class="panel front-cover" aria-label="Main cover">
  <svg class="sun-art" style="left:110px;top:82px" width="190" height="190" viewBox="0 0 190 190" role="img" aria-label="Watercolour sun with a sketched grand piano">
    <defs>
      <linearGradient id="sunFront" x1="0" y1="0" x2="0" y2="1">
        <stop offset="0" stop-color="var(--sun-top)"/>
        <stop offset=".55" stop-color="var(--sun-mid)"/>
        <stop offset="1" stop-color="var(--sun-low)"/>
      </linearGradient>
    </defs>
    <circle cx="95" cy="95" r="93" fill="url(#sunFront)"/>
  </svg>
  <div class="heading">
    <p class="album-title">Gentle Willow II.</p>
    <p class="album-artist">Ember Reed Trio</p>
  </div>
</section>

<section class="panel back-cover" aria-label="Back cover">
  <svg class="sun-art" style="left:0;top:0" width="270" height="240" viewBox="0 0 270 240" role="img" aria-label="Watercolour sun with a sketched grand piano">
    <defs>
      <linearGradient id="sunBack" x1="0" y1="0" x2="0" y2="1">
        <stop offset="0" stop-color="var(--sun-top)"/>
        <stop offset=".55" stop-color="var(--sun-mid)"/>
        <stop offset="1" stop-color="var(--sun-low)"/>
      </linearGradient>
    </defs>
    <circle cx="130" cy="100" r="135" fill="url(#sunBack)"/>
  </svg>
  <div class="side-heading">
    <p class="album-title">Gentle Willow II.</p>
    <p class="album-artist">Ember Reed Trio</p>
    <p class="credits">All songs written by Bence Morvath<br>Copyright Velmorsound 2016</p>
  </div>
  <p class="web-address">www.velmorsound.com</p>
  <ol class="track-list">
    <li><span class="track-no">1</span><span>First, in G</span><span class="track-time">05:08</span></li>
    <li><span class="track-no">2</span><span>Second, in Em</span><span class="track-time">05:11</span></li>
    <li><span class="track-no">3</span><span>Third, in G</span><span class="track-time">05:09</span></li>
    <li><span class="track-no">4</span><span>Fourth, in A</span><span class="track-time">05:07</span></li>
    <li><span class="track-no">5</span><span>Fifth, in Bm</span><span class="track-time">05:01</span></li>
    <li><span class="track-no">6</span><span>Sixth, in A</span><span class="track-time">05:11</span></li>
    <li><span class="track-no">7</span><span>Seventh, in G</span><span class="track-time">05:07</span></li>
    <li><span class="track-no">8</span><span>Eighth, in Bm</span><span class="track-time">05:06</span></li>
    <li><span class="track-no">9</span><span>Ninth, in Gm</span><span class="track-time">05:04</span></li>
    <li><span class="track-no">10</span><span>Tenth, in E</span><span class="track-time">05:03</span></li>
    <li><span class="track-no">11</span><span>Eleventh, in G</span><span class="track-time">05:12</span></li>
    <li><span class="track-no">12</span><span>Twelfth, in A</span><span class="track-time">05:09</span></li>
    <li><span class="track-no">13</span><span>Thirteenth, in E</span><span class="track-time">05:10</span></li>
    <li><span class="track-no">14</span><span>Fourteenth, in Am</span><span class="track-time">05:14</span></li>
    <li><span class="track-no">15</span><span>Fifteenth, in F</span><span class="track-time">05:05</span></li>
    <li><span class="track-no">16</span><span>Sixteenth, in Am</span><span class="track-time">05:05</span></li>
    <li><span class="track-no">17</span><span>Seventeenth, in F</span><span class="track-time">05:04</span></li>
    <li><span class="track-no">18</span><span>Eighteenth, in D</span><span class="track-time">05:07</span></li>
  </ol>
</section>

<section class="panel inside-cover" aria-label="Inside cover">
  <svg class="sun-art" style="left:0;top:0" width="240" height="240" viewBox="0 0 240 240" role="img" aria-label="Watercolour sun with a sketched grand piano">
    <defs>
      <linearGradient id="sunInside" x1="0" y1="0" x2="0" y2="1">
        <stop offset="0" stop-color="var(--sun-top)"/>
        <stop offset=".55" stop-color="var(--sun-mid)"/>
        <stop offset="1" stop-color="var(--sun-low)"/>
      </linearGradient>
    </defs>
    <circle cx="110" cy="105" r="135" fill="url(#sunInside)"/>
  </svg>
  <div class="side-heading">
    <p class="album-title">Gentle Willow II.</p>
    <p class="album-artist">Ember Reed Trio</p>
    <p class="credits">All songs written by Bence Morvath<br>Copyright Velmorsound 2016</p>
  </div>
  <ol class="track-list">
    <li><span class="track-no">1</span><span>First, in G</span><span class="track-time">05:08</span></li>
    <li><span class="track-no">2</span><span>Second, in Em</span><span class="track-time">05:11</span></li>
    <li><span class="track-no">3</span><span>Third, in G</span><span class="track-time">05:09</span></li>
    <li><span class="track-no">4</span><span>Fourth, in A</span><span class="track-time">05:07</span></li>
    <li><span class="track-no">5</span><span>Fifth, in Bm</span><span class="track-time">05:01</span></li>
    <li><span class="track-no">6</span><span>Sixth, in A</span><span class="track-time">05:11</span></li>
    <li><span class="track-no">7</span><span>Seventh, in G</span><span class="track-time">05:07</span></li>
    <li><span class="track-no">8</span><span>Eighth, in Bm</span><span class="track-time">05:06</span></li>
    <li><span class="track-no">9</span><span>Ninth, in Gm</span><span class="track-time">05:04</span></li>
    <li><span class="track-no">10</span><span>Tenth, in E</span><span class="track-time">05:03</span></li>
    <li><span class="track-no">11</span><span>Eleventh, in G</span><span class="track-time">05:12</span></li>
    <li><span class="track-no">12</span><span>Twelfth, in A</span><span class="track-time">05:09</span></li>
    <li><span class="track-no">13</span><span>Thirteenth, in E</span><span class="track-time">05:10</span></li>
    <li><span class="track-no">14</span><span>Fourteenth, in Am</span><span class="track-time">05:14</span></li>
    <li><span class="track-no">15</span><span>Fifteenth, in F</span><span class="track-time">05:05</span></li>
    <li><span class="track-no">16</span><span>Sixteenth, in Am</span><span class="track-time">05:05</span></li>
    <li><span class="track-no">17</span><span>Seventeenth, in F</span><span class="track-time">05:04</span></li>
    <li><span class="track-no">18</span><span>Eighteenth, in D</span><span class="track-time">05:07</span></li>
  </ol>
</section>

<section class="tray" aria-label="Under the disc">
  <svg width="480" height="404" viewBox="0 0 480 404">
    <defs>
      <radialGradient id="washYellow" cx=".35" cy=".4" r=".7">
        <stop offset="0" stop-color="var(--wash-yellow)"/>
        <stop offset=".75" stop-color="var(--wash-yellow)" stop-opacity=".85"/>
        <stop offset="1" stop-color="var(--wash-yellow)" stop-opacity="0"/>
      </radialGradient>
      <radialGradient id="washPink" cx=".45" cy=".5" r=".65">
        <stop offset="0" stop-color="var(--wash-pink)"/>
        <stop offset=".8" stop-color="var(--wash-pink)" stop-opacity=".85"/>
        <stop offset="1" stop-color="var(--wash-pink)" stop-opacity="0"/>
      </radialGradient>
    </defs>
    <g role="img" aria-label="Soft yellow and pink watercolour washes">
      <ellipse cx="90" cy="110" rx="150" ry="120" fill="url(#washYellow)"/>
      <ellipse cx="390" cy="330" rx="110" ry="95" fill="url(#washPink)"/>
    </g>
    <circle cx="275" cy="205" r="190" fill="none" stroke="var(--tray-line)" stroke-width="1.5"/>
    <circle cx="275" cy="205" r="40" fill="rgba(255,255,255,.5)" stroke="var(--tray-line)" stroke-width="2"/>
    <circle cx="275" cy="205" r="22" fill="none" stroke="var(--tray-line)" stroke-width="1.5"/>
  </svg>
</section>

<svg class="disc" viewBox="0 0 420 420" aria-label="Disc label">
  <defs>
    <clipPath id="discShape"><circle cx="210" cy="210" r="202"/></clipPath>
    <linearGradient id="sunDisc" x1="0" y1="0" x2="0" y2="1">
      <stop offset="0" stop-color="var(--sun-top)"/>
      <stop offset=".55" stop-color="var(--sun-mid)"/>
      <stop offset="1" stop-color="var(--sun-low)"/>
    </linearGradient>
    <radialGradient id="discPaper" cx=".45" cy=".4" r=".7">
      <stop offset=".6" stop-color="var(--paper)"/>
      <stop offset="1" stop-color="var(--paper-edge)"/>
    </radialGradient>
    <path id="rimText" d="M30,210 A180,180 0 1,0 390,210 A180,180 0 1,0 30,210"/>
  </defs>
  <circle cx="210" cy="210" r="203" fill="#fff" opacity=".6"/>
  <g clip-path="url(#discShape)">
    <circle cx="210" cy="210" r="202" fill="url(#discPaper)"/>
    <circle cx="132" cy="140" r="128" fill="url(#sunDisc)" role="img" aria-label="Watercolour sun with a sketched grand piano"/>
  </g>
  <circle cx="210" cy="210" r="62" fill="none" stroke="#b9b5ab" stroke-width="1"/>
  <circle cx="210" cy="210" r="46" fill="var(--backdrop)"/>
  <text x="210" y="300" text-anchor="middle" font-family="Montserrat, Arial, sans-serif" font-size="15" font-weight="400" fill="var(--ink)">Gentle Willow II.</text>
  <text x="210" y="326" text-anchor="middle" font-family="Montserrat, Arial, sans-serif" font-size="23" font-weight="300" fill="#333">Ember Reed Trio</text>
  <text font-family="Montserrat, Arial, sans-serif" font-size="9.5" fill="var(--ink)">
    <textPath href="#rimText" startOffset="4%">All songs written by <tspan font-weight="700">Bence Morvath</tspan></textPath>
  </text>
  <text font-family="Montserrat, Arial, sans-serif" font-size="9.5" fill="var(--ink)">
    <textPath href="#rimText" startOffset="29%">Copyright <tspan font-weight="700">Velmorsound 2016</tspan></textPath>
  </text>
  <text font-family="Montserrat, Arial, sans-serif" font-size="9.5" font-weight="700" fill="var(--ink)">
    <textPath href="#rimText" startOffset="45%">www.velmorsound.com</textPath>
  </text>
</svg>

</body>
</html>
```